LUMA Neighborhood Aid for Critter Welfare

LUMA SCS PET OWNERS WITH VACCINATIONS, MICROCHIP, Spay & NEUTER, TRANSPORTATION FOR PET OWNERS THAT ARE ELDERLY OR MOBILITY CHALLENGED, PET SITTING, PET GROOMING, EDUCATION, adoption counseling, grief counseling, in-home evaluations, feral trap and release, public speaking on education of pet ownership, seminars, meetings and outreach. LUMA depends 100% on donations. I need the webpage to be able to link up to my PayPal account for donations. Serving the greater Houston area.

Reason: My dog of 15 yrs is dying.

```html
<!DOCTYPE html>
<html lang="en">
<head>
<meta charset="utf-8">
<title>LUMA — Neighborhood Aid for Critter Welfare</title>
<link href="https://fonts.googleapis.com/css2?family=Arimo:wght@400;700&family=Lato:wght@400;700&family=Tinos:ital@1&display=swap" rel="stylesheet">
<style>
:root{
  --coral:#e5604a;
  --amber:#f6b733;
  --teal:#16a88a;
  --teal-soft:#2fbf9f;
  --ink:#555555;
  --white:#ffffff;
  --footer:#4a4a4a;
  --footer-dark:#3d3d3d;
  --footer-text:#e4e4e4;
  --button-grey:#e6e8ea;
}
*{margin:0;padding:0;box-sizing:border-box}
html,body{width:710px;height:1200px;overflow:hidden;background:var(--white)}
body{position:relative;font-family:"Arimo",Arial,sans-serif;color:var(--ink)}
.abs{position:absolute}

/* header */
.site-header{left:0;top:0;width:710px;height:45px;background:var(--coral)}
.brand{left:102px;top:11px;display:flex;align-items:center;gap:5px;color:var(--white);font-weight:700;font-size:17px;letter-spacing:.5px}
.brand-dot{width:9px;height:9px;border-radius:50%;background:var(--white)}
.main-nav{top:20px;font-size:7.5px;color:var(--white);letter-spacing:.2px}

/* hero */
.hero{left:0;top:45px;width:710px;height:307px;background:linear-gradient(110deg,#8a8a8a 0%,#b9b9b9 30%,#5b5b5b 55%,#2e2e2e 75%,#9a9a9a 100%)}
.hero-arrow{top:150px}
.hero-badge{left:101px;top:100px;width:216px;height:216px;border-radius:50%;background:rgba(47,191,159,.75)}
.hero-badge-inner{left:113px;top:112px;width:192px;height:192px;border-radius:50%;background:var(--teal)}
.hero-text{left:113px;width:192px;text-align:center;color:var(--white)}
.hero-kicker{top:153px;font-size:14px;letter-spacing:.5px}
.hero-lead{top:170px;font-family:"Tinos","Times New Roman",serif;font-style:italic;font-size:21px;line-height:22px}
.hero-rule{left:141px;top:227px;width:136px;height:3px;border-top:1px solid var(--white);border-bottom:1px solid var(--white)}
.hero-sub{top:238px;font-size:11.5px;line-height:17px}

/* services */
.service{top:362px;width:169px;height:84px;padding:14px 18px;color:var(--white)}
.service h3{font-size:8px;font-weight:400;letter-spacing:.3px;padding-bottom:5px;border-bottom:1px solid var(--white);width:88px;margin-bottom:8px}
.service p{font-size:5.8px;line-height:11.5px}
.service-1{left:102px;background:var(--coral)}
.service-2{left:271px;background:var(--amber)}
.service-3{left:440px;background:var(--teal)}

/* what we do */
.section-title{color:var(--coral);font-size:16px;font-weight:400;letter-spacing:.3px}
.wwd-title{top:477px;left:0;width:710px;text-align:center}
.wwd-intro{left:130px;top:508px;width:450px;text-align:center;font-size:6.3px;line-height:13.2px}
.offer-title{top:569px;color:var(--coral);font-size:9px}
.offer-photo{top:590px;width:153px;height:92px}
.offer-text{top:691px;width:155px;font-size:6.3px;line-height:13px}

/* videos */
.video-frame{left:102px;top:774px;width:249px;height:152px;background:linear-gradient(120deg,#2a1d10 0%,#6b4a22 45%,#a0762f 60%,#3a2812 100%)}
.video-play{left:212px;top:836px}
.video-bar{left:104px;top:912px;width:245px;height:12px;background:rgba(0,0,0,.7)}
.videos-title{left:380px;top:776px}
.videos-text{left:380px;top:800px;width:222px;font-family:"Lato",Arial,sans-serif;font-size:6.4px;line-height:13.6px}
.btn-coral{left:381px;top:894px;width:122px;height:25px;background:var(--coral);color:var(--white);font-size:8px;display:flex;align-items:center;justify-content:center;text-decoration:none;border-radius:1px}

/* transport band */
.transport-band{left:0;top:972px;width:710px;height:49px;background:var(--coral)}
.transport-text{left:110px;top:990px;color:var(--white);font-size:11.5px}
.btn-donate{left:498px;top:984px;width:111px;height:26px;background:var(--button-grey);color:#555;font-size:9px;display:flex;align-items:center;justify-content:center;text-decoration:none;border-radius:2px;box-shadow:0 1px 1px rgba(0,0,0,.2)}

/* footer */
.site-footer{left:0;top:1021px;width:710px;height:149px;background:var(--footer);font-family:"Lato",Arial,sans-serif;color:var(--footer-text)}
.footer-col{top:1042px}
.footer-col h4{font-size:7.5px;font-weight:700;color:var(--white);margin-bottom:9px;letter-spacing:.2px}
.footer-col li{list-style:none;font-size:6.5px;line-height:15.2px}
.contact-item{display:flex;gap:6px;font-size:6.5px;line-height:10.5px;margin-bottom:5px}
.contact-item svg{flex:none;margin-top:2px}
.social-item{display:flex;align-items:center;gap:4px;font-size:6.5px;margin-bottom:5.5px}
.social-ring{width:15px;height:15px;border:1px solid #9a9a9a;border-radius:50%}
.footer-bottom{left:0;top:1170px;width:710px;height:30px;background:var(--footer-dark);color:#dcdcdc;font-family:"Lato",Arial,sans-serif;font-size:6px;display:flex;align-items:center;justify-content:center}
</style>
</head>
<body>

<header class="abs site-header">
  <div class="abs brand"><span class="brand-dot"></span>LUMA</div>
  <nav>
    <span class="abs main-nav" style="left:278px">HOME</span>
    <span class="abs main-nav" style="left:330px">ABOUT</span>
    <span class="abs main-nav" style="left:386px">SERVICES</span>
    <span class="abs main-nav" style="left:453px">STAFF</span>
    <span class="abs main-nav" style="left:506px">TESTIMONIALS</span>
    <span class="abs main-nav" style="left:589px">BLOG</span>
  </nav>
</header>

<section class="abs hero" role="img" aria-label="Black and white close-up photo of a cat"></section>
<svg class="abs hero-arrow" style="left:40px" width="18" height="70" viewBox="0 0 18 70"><path d="M16 2 L2 35 L16 68" fill="none" stroke="rgba(255,255,255,.6)" stroke-width="1"/></svg>
<svg class="abs hero-arrow" style="left:664px" width="18" height="70" viewBox="0 0 18 70"><path d="M2 2 L16 35 L2 68" fill="none" stroke="rgba(255,255,255,.6)" stroke-width="1"/></svg>
<div class="abs hero-badge"></div>
<div class="abs hero-badge-inner"></div>
<div class="abs hero-text hero-kicker">WE PROVIDE</div>
<div class="abs hero-text hero-lead">Pet owners with<br>vaccinations</div>
<div class="abs hero-rule"></div>
<div class="abs hero-text hero-sub">MICROCHIP,<br>SPAY &amp; NEUTER</div>

<div class="abs service service-1"><h3>SERVICES 01</h3><p>Lorem Ipsum is simply dummy text of the printing and typesetting industry. Lorem Ipsum has been the industry's standard dummy...</p></div>
<div class="abs service service-2"><h3>SERVICES 02</h3><p>Lorem Ipsum is simply dummy text of the printing and typesetting industry. Lorem Ipsum has been the industry's standard dummy...</p></div>
<div class="abs service service-3"><h3>SERVICES 03</h3><p>Lorem Ipsum is simply dummy text of the printing and typesetting industry. Lorem Ipsum has been the industry's standard dummy...</p></div>

<h2 class="abs section-title wwd-title">WHAT WE DO</h2>
<p class="abs wwd-intro">Lorem Ipsum is simply dummy text of the printing and typesetting industry. Lorem Ipsum has been the industry's standard dummy text ever since the 1500s, when an unknown printer took a galley of type and scrambled it to make a type specimen book. It has survived not only five centuries, but also the leap into electronic typesetting, remaining essentially unchanged.</p>

<h3 class="abs offer-title" style="left:102px">PET SITTING</h3>
<div class="abs offer-photo" style="left:102px;background:linear-gradient(160deg,#c9a46a,#e7d6b4 50%,#8d6d43)" role="img" aria-label="Photo of two kittens in a cardboard box"></div>
<p class="abs offer-text" style="left:102px">Lorem Ipsum is simply dummy text of the printing and typesetting industry. Lorem Ipsum has been the industry's standard dummy text ever...</p>

<h3 class="abs offer-title" style="left:280px">PET GROOMING</h3>
<div class="abs offer-photo" style="left:279px;background:linear-gradient(100deg,#d9c29a,#f1efe9 50%,#3b7fc0)" role="img" aria-label="Photo of a groomer holding a small fluffy dog"></div>
<p class="abs offer-text" style="left:279px">Lorem Ipsum is simply dummy text of the printing and typesetting industry. Lorem Ipsum has been the industry's standard dummy text ever...</p>

<h3 class="abs offer-title" style="left:457px">EDUCATION</h3>
<div class="abs offer-photo" style="left:456px;background:linear-gradient(180deg,#7fa04a,#a88a5c 45%,#5d8a35)" role="img" aria-label="Photo of a beagle carrying a ball on grass"></div>
<p class="abs offer-text" style="left:456px">Lorem Ipsum is simply dummy text of the printing and typesetting industry. Lorem Ipsum has been the industry's standard dummy text ever...</p>

<div class="abs video-frame" role="img" aria-label="Video still of a lion with an inspirational quote"></div>
<svg class="abs video-play" width="28" height="28" viewBox="0 0 28 28"><circle cx="14" cy="14" r="13" fill="rgba(255,255,255,.35)"/><path d="M11 8 L20 14 L11 20Z" fill="rgba(60,60,60,.7)"/></svg>
<div class="abs video-bar"></div>
<svg class="abs" style="left:108px;top:914px" width="240" height="8" viewBox="0 0 240 8"><path d="M4 1 L9 4 L4 7Z" fill="#fff"/><rect x="24" y="3" width="170" height="2" fill="#777"/><rect x="200" y="2" width="12" height="4" fill="#5aa9d6"/></svg>

<h2 class="abs section-title videos-title">VIDEOS</h2>
<p class="abs videos-text">Lorem Ipsum is simply dummy text of the printing and typesetting industry. Lorem Ipsum has been the industry's standard dummy text ever since the 1500s, when an unknown printer took a galley of type and scrambled it to make a type specimen book. It has survived not only five centuries, but also the leap into electronic typesetting, remaining essentially unchanged...</p>
<a class="abs btn-coral" href="#videos">VIEW MORE VIDEOS</a>

<div class="abs transport-band"></div>
<p class="abs transport-text">We give transportation to pet owners who are elderly or mobility challenged</p>
<a class="abs btn-donate" href="#donate">DONATE HERE</a>

<footer class="abs site-footer"></footer>
<div class="abs footer-col" style="left:128px;color:var(--footer-text)">
  <h4>WELCOME</h4>
  <ul><li>Home</li><li>About</li><li>Services</li><li>Staff</li><li>Testimonials</li><li>Blog</li></ul>
</div>
<div class="abs footer-col" style="left:234px;color:var(--footer-text);font-family:Lato,sans-serif">
  <h4>INFORMATION</h4>
  <ul><li>Terms &amp; Conditions</li><li>Privacy Policy</li><li>Sitemap</li></ul>
</div>
<div class="abs footer-col" style="left:350px;color:var(--footer-text);font-family:Lato,sans-serif">
  <h4>CONTACT</h4>
  <div class="contact-item"><svg width="6" height="8" viewBox="0 0 6 8"><path d="M3 0a3 3 0 0 0-3 3c0 2 3 5 3 5s3-3 3-5a3 3 0 0 0-3-3z" fill="#bbb"/></svg><span>120 Streat name, State name,<br>Country name.</span></div>
  <div class="contact-item"><svg width="6" height="8" viewBox="0 0 6 8"><rect x=".5" y=".5" width="5" height="7" rx="1" fill="none" stroke="#bbb"/></svg><span>(713) 555 0142</span></div>
  <div class="contact-item"><svg width="6" height="8" viewBox="0 0 6 8"><rect x="0" y="3" width="6" height="4" fill="#bbb"/><rect x="1" y="1" width="4" height="2" fill="#bbb"/></svg><span>(713) 555 0143</span></div>
  <div class="contact-item"><svg width="7" height="8" viewBox="0 0 7 8"><rect x=".5" y="2" width="6" height="4.5" fill="none" stroke="#bbb"/><path d="M.5 2 L3.5 4.5 L6.5 2" fill="none" stroke="#bbb"/></svg><span>hello@luma-aid.org</span></div>
</div>
<div class="abs footer-col" style="left:507px;color:var(--footer-text);font-family:Lato,sans-serif">
  <h4>FOLLOW US</h4>
  <div class="social-item"><span class="social-ring"></span>: Pawbook</div>
  <div class="social-item"><span class="social-ring"></span>: Chirper</div>
  <div class="social-item"><span class="social-ring"></span>: Linkline</div>
  <div class="social-item"><span class="social-ring"></span>: Petplus</div>
</div>
<div class="abs footer-bottom">© Copyrights 2014 LUMA. All rights reserved.</div>

</body>
</html>
```